Podcast Cover Art for Fast Growing Show (Ill include a gracious tip!)

This artwork is for "The Steadfast Fellow Show." The podcast is for men, and it's all about self-improvement, confidence, success, money, women and masculinity. It's for the guy who wants to improve himself. I'd like for my picture to be included — in black and white — and I want the text to read: "The Steadfast Fellow Show" and somewhere in there it'll say: "with Dale Prowen." I'm open to color schemes. The podcast is a little edgy so I'd like for that to be represented in the design. Thank you! (((Here's the podcast page if you wanna check it out: http://steadfastfellowshow.castorbit.net/)))

Target Market(s)

Men who want to attract women and improve their lives!

Font styles to use
Serif

Colors

Designer to choose colors to be used in the design.

Requirements
Must have
• My image in it (in black and white) and the two titles: "The Steadfast Fellow Show" and "with Dale Prowen"
Nice to have
• My logo in it somehow (which is the arrow looking logo attached below). I've also found that my image looks best in black and white and with a circular type cut out (although I'm open to different design ideas). I've attached my logo with a circular cut out below so you can see what I'm talking about.
Should not have
• Flowers. Teddy bears. ice cream.

```html
<!DOCTYPE html>
<html lang="en">
<head>
<meta charset="utf-8">
<title>The Steadfast Fellow Show — Cover Art</title>
<link rel="stylesheet" href="https://fonts.googleapis.com/css2?family=Crimson+Pro:wght@400&family=Roboto:wght@400&display=swap">
<style>
  :root {
    --bg: #454545;
    --frame: #141414;
    --panel: #ffffff;
    --ink: #0d0d0d;
    --mark: #ffffff;
    --photo-light: #6a6a6a;
    --photo-dark: #1c1c1c;
  }
  html, body {
    margin: 0;
    padding: 0;
    overflow: hidden;
    background: var(--bg);
  }
  .cover {
    position: relative;
    width: 1200px;
    height: 1200px;
    background: var(--bg);
    overflow: hidden;
  }
  .title-card {
    position: absolute;
    left: 153px;
    top: 186px;
    width: 703px;
    height: 536px;
    box-sizing: border-box;
    border: 9px solid var(--frame);
    background: var(--frame);
    display: flex;
    flex-direction: column;
    gap: 9px;
  }
  .title-card__main {
    background: var(--panel);
    height: 400px;
    position: relative;
  }
  .show-title {
    position: absolute;
    left: 35px;
    top: 20px;
    margin: 0;
    font-family: "Crimson Pro", Georgia, serif;
    font-weight: 400;
    font-size: 122px;
    line-height: 124px;
    color: var(--ink);
    letter-spacing: -1px;
  }
  .show-title span { display: block; }
  .title-card__host {
    background: var(--panel);
    flex: 1;
    display: flex;
    align-items: center;
    padding-left: 35px;
  }
  .host-line {
    margin: 0;
    font-family: "Roboto", Arial, sans-serif;
    font-size: 46px;
    color: var(--ink);
  }
  .brand-mark {
    position: absolute;
    left: 87px;
    top: 1074px;
    display: flex;
    align-items: center;
    gap: 12px;
    font-family: "Crimson Pro", Georgia, serif;
    font-size: 34px;
    color: var(--mark);
  }
  .brand-mark__square {
    width: 26px;
    height: 26px;
    background: var(--mark);
  }
  .host-photo {
    position: absolute;
    left: 880px;
    top: 232px;
    width: 320px;
    height: 968px;
    border-top-left-radius: 180px;
    background: linear-gradient(160deg, var(--photo-light) 0%, #3a3a3a 45%, var(--photo-dark) 100%);
  }
</style>
</head>
<body>
  <main class="cover">
    <section class="title-card">
      <div class="title-card__main">
        <h1 class="show-title">
          <span>The</span>
          <span>Steadfast</span>
          <span>Fellow Show</span>
        </h1>
      </div>
      <div class="title-card__host">
        <p class="host-line">w/ Dale Prowen</p>
      </div>
    </section>

    <div class="brand-mark">
      <span class="brand-mark__square"></span>
      <span>Steadfast</span>
    </div>

    <div class="host-photo" role="img" aria-label="Black and white portrait of host Dale Prowen, hand raised to his chin"></div>
  </main>
</body>
</html>
```